Meridian Swift add on sales tool2017

This will be a flyer to leave with our clients we just did work for. We want to entice them to use our other services over the next 30 days with a discount, money off etc. we will write in the special and the expiration date. I want the client to read the description and see a picture of the service they may want done.

Target Market(s)

Repeat clients

Industry/Entity Type

Cleaning Service

Font styles to use
Serif
Sans Serif

Colors
ec1f27
000000
b1b1b1

Requirements
Must have
• Call to action! look high end market, clients show we do 1st class work.
• Don't Waite
Nice to have
• Classy, quality, I'm open to using other pictures that may look better
Should not have
• Look like a typical carpet cleaners special flyer
• Not to look cluttered

```html
<!DOCTYPE html>
<html lang="en">
<head>
<meta charset="utf-8">
<title>Meridian Swift – 30 Days Special Offer</title>
<link href="https://fonts.googleapis.com/css2?family=Lato:wght@400;700;900&family=Arimo:wght@400;700&display=swap" rel="stylesheet">
<style>
  :root{
    --red:#ec1f27;
    --black:#000000;
    --grey:#b1b1b1;
    --grey-dark:#a5a5a5;
    --hero:#2e2e2e;
    --white:#ffffff;
    --ink:#1a1a1a;
  }
  *{margin:0;padding:0;box-sizing:border-box}
  html,body{width:1200px;height:1200px;overflow:hidden;background:#e9e9e9}
  .stage{position:relative;width:1200px;height:1200px}
  .flyer{
    position:absolute;left:186px;top:20px;width:1002px;height:1405px;
    transform:scale(0.8256);transform-origin:top left;
    background:var(--white);font-family:"Lato",sans-serif;color:var(--ink);
    box-shadow:0 6px 22px rgba(0,0,0,.25);overflow:hidden;
  }
  .top-strip{position:absolute;left:0;top:0;width:100%;height:14px;background:var(--black)}
  .brand{position:absolute;left:37px;top:22px;width:156px;display:flex;flex-direction:column;align-items:center;gap:8px}
  .brand-dot{width:46px;height:46px;border-radius:50%;background:var(--red)}
  .brand-name{font-family:"Lato",sans-serif;font-weight:900;font-size:15px;color:var(--red);letter-spacing:.6px;white-space:nowrap;line-height:1}
  .tagline{position:absolute;left:212px;top:38px;font-family:"Arimo",sans-serif;font-weight:700;font-size:36px;color:var(--red);white-space:nowrap}

  .hero{position:absolute;left:0;top:105px;width:100%;height:393px;background:linear-gradient(135deg,#3a3a3a,#242424 55%,#333)}
  .hero-frame{position:absolute;left:23px;top:20px;width:954px;height:353px;border:2px dashed #cfcfcf}
  .offer{position:absolute;left:0;right:0;top:48px;text-align:center;font-weight:900;font-size:82px;color:var(--red);letter-spacing:-1px;line-height:1}
  .call{position:absolute;left:0;right:0;top:146px;text-align:center;font-weight:700;font-size:50px;color:var(--white);line-height:1}
  .pill{position:absolute;left:72px;width:858px;height:47px;border-radius:24px;background:var(--white);
        font-weight:700;font-size:23px;color:var(--ink);padding-left:31px;line-height:47px}
  .pill.expires{top:228px}
  .pill.blank{top:298px}

  .gallery{position:absolute;left:30px;top:498px;width:347px;height:819px;background:var(--grey-dark)}
  .shot{position:absolute;left:11px;width:323px;border:3px solid var(--black);overflow:hidden}
  .shot .label{position:absolute;bottom:10px;font-family:"Arimo",sans-serif;font-weight:700;font-size:19px;color:var(--white)}
  .half{position:absolute;top:0;bottom:0;width:50%}
  .divider{position:absolute;top:0;bottom:0;left:50%;width:3px;margin-left:-1px;background:var(--white)}

  .services{position:absolute;left:408px;top:0;width:580px}
  .service{position:absolute;left:0;width:580px}
  .service h2{font-weight:700;font-size:25px;color:var(--red);letter-spacing:-.3px;line-height:1;margin-bottom:14px;white-space:nowrap}
  .service p{font-size:20px;line-height:26px;color:var(--ink);white-space:nowrap}

  .footer{position:absolute;left:0;bottom:0;width:100%;height:71px;background:var(--red);display:flex;align-items:center;
          padding-left:36px;font-family:"Arimo",sans-serif;font-size:23px;color:var(--white);white-space:nowrap}
  .footer svg{flex:none}
  .footer .sep{margin:0 22px 0 32px}
  .footer .item{margin-left:14px}
</style>
</head>
<body>
<div class="stage">
  <article class="flyer">
    <div class="top-strip"></div>

    <header>
      <div class="brand"><span class="brand-dot"></span><span class="brand-name">MERIDIAN SWIFT</span></div>
      <p class="tagline">One Stop For All Your Home Cleaning Needs</p>
    </header>

    <section class="hero" role="img" aria-label="Technician in work clothes cleaning with a hose wand, darkened background photo">
      <div class="hero-frame"></div>
      <h1 class="offer">30 Days Special Offer!</h1>
      <p class="call">Call now to book 702-555-0147</p>
      <div class="pill expires">Expires -</div>
      <div class="pill blank"></div>
    </section>

    <aside class="gallery">
      <div class="shot" style="top:17px;height:146px;background:linear-gradient(160deg,#d2bfa2,#b89f7e)" role="img" aria-label="Carpet cleaning wand on a beige carpet"></div>
      <div class="shot" style="top:184px;height:135px">
        <div class="half" style="left:0;background:linear-gradient(180deg,#8a8a80,#4d4d47)" role="img" aria-label="Upholstery before cleaning"></div>
        <div class="half" style="left:50%;background:linear-gradient(180deg,#d8d6cc,#6b3d3a)" role="img" aria-label="Upholstery after cleaning"></div>
        <div class="divider"></div>
        <span class="label" style="left:58px">Before</span><span class="label" style="left:216px">After</span>
      </div>
      <div class="shot" style="top:340px;height:143px;background:linear-gradient(180deg,#8f766c,#3b322e 60%,#b9bcbf)" role="img" aria-label="Technician cleaning drapes at a window"></div>
      <div class="shot" style="top:504px;height:135px">
        <div class="half" style="left:0;background:linear-gradient(150deg,#7d7a80,#55524f)" role="img" aria-label="Tile and grout before cleaning"></div>
        <div class="half" style="left:50%;background:linear-gradient(150deg,#cfc9c4,#a49d97)" role="img" aria-label="Tile and grout after cleaning"></div>
        <div class="divider"></div>
        <span class="label" style="left:58px">Before</span><span class="label" style="left:216px">After</span>
      </div>
      <div class="shot" style="top:665px;height:144px;background:linear-gradient(180deg,#c8c8c4,#8c8985 50%,#d9d7d3)" role="img" aria-label="Polished marble floor in a bright room"></div>
    </aside>

    <main class="services">
      <section class="service" style="top:527px">
        <h2>CARPET CLEANING</h2>
        <p>Don't let dirty carpets spoil the look of your beautiful home!.<br>with 37 years of cleaning carpets experienceyou can expect<br>your carpets to look like new in most cases.</p>
      </section>
      <section class="service" style="top:696px">
        <h2>UPHOLSTERY CLEANING</h2>
        <p>Every day use leaves your sofa's and chairs lookng dingy<br>and can smell like dog. Our Dry cleaning ,Shampoo or<br>Rinse extraxtion will leave the fabric feel like clean sheet!</p>
      </section>
      <section class="service" style="top:843px">
        <h2>DARAPERY CLEANING</h2>
        <p>Drapery's act like a filter atracting atmisphiric soil! &nbsp;Making<br>them look dingy, We make it easy to Dry clean in-home! Safe<br>and efective beautiful drapery again.</p>
      </section>
      <section class="service" style="top:1009px">
        <h2>TILE &amp; GROUT CLEANING</h2>
        <p>Tile &amp; Grout get neglected! Dirty grout can leave<br>permanent staining. Let our professionals bring back the<br>look of a new floor.</p>
      </section>
      <section class="service" style="top:1180px">
        <h2>NATURAL STONE CLEANING &amp; POLISHING</h2>
        <p>A dull stained Marble - Granite-Travertine and other Natural<br>stone can be revitalized to look.NEW again!</p>
      </section>
    </main>

    <footer class="footer">
      <svg width="16" height="20" viewBox="0 0 16 20" aria-hidden="true"><path d="M8 0a8 8 0 0 0-8 8c0 6 8 12 8 12s8-6 8-12a8 8 0 0 0-8-8z" fill="#fff"/><circle cx="8" cy="8" r="3" fill="#ec1f27"/></svg>
      <span class="item">1480 W. Sandstone Ave. Suite C ,Las Vegas</span>
      <span class="sep">|</span>
      <svg width="20" height="20" viewBox="0 0 20 20" aria-hidden="true"><circle cx="10" cy="10" r="9" fill="none" stroke="#fff" stroke-width="2"/><ellipse cx="10" cy="10" rx="4" ry="9" fill="none" stroke="#fff" stroke-width="1.6"/><line x1="1" y1="10" x2="19" y2="10" stroke="#fff" stroke-width="1.6"/></svg>
      <span class="item">www.meridianswiftcleaners.com</span>
    </footer>
  </article>
</div>
</body>
</html>
```